School Design and Build Sales Brochure

I am looking for a 4 page (Be printed as A3 and folded in half) A4 Brochure I have attached a word document with basic layout, wording and some photos I want included in the brochure. The word document is only a very rough rough guide. I am looking for a designer to really put together something unique and eye catching that will work in getting peoples attention when arriving through the post.

I have also attached a zip file with more photos that can be added to the the brochure should your design lend itself to it.

I have attached logo, business card and letterhead to give you an idea of company colours/ identity but don't feel restricted by this. The brochure is stand alone and there to bring in new customers

I have also posted a website contest for the above company and you can have a look at that informationa as well.

Pages 2-3 of Brochure can be treated as A3 to allow more flexibility when laying out those pages.

Good luck and I look forward to seeing the results.

I use www.quellprintworks.co.uk for my printing so templates / standards / formats for prinitng can be found there.

Dear All,

Further to your comments I have uploaded a .zip file with all photos from the word document.

As for the vector file I don't seem to have it but it was donw by a designer on artmarrow I have asked them to send me a copy. As soon as I have it I will upload it.

The first design submitted was very poor, but I am sure much better is to follow.

Kind regards,

Gideon

Dear All,

Vector file for the logo has now been uploaded.

Kind regards,

Gideon

Dear All,

I am not really "feeling" any of the brochures submitted to date, I like some of the design ideas but something is not right. I believe this is because my brief is not quite right. You are producing what I asked for but having looked at it again I would like to make the following changes to the brief,

1. I think there is too much writing. I have uploaded a new word document with the only writing I want on the brochure. I think this will allow more space for photos / design.

The writing must appear on the following pages,

1. About Us - On The Front Page
2. Services we Provide -   On the front page or two middle pages
3. Client List :  On the back page.

2. The front page must have photos on. I would say two at minimum.

Thank you for your efforts so far, I look forward to recieving revised designs.
Kind regards,

Gideon

Target Market(s)

Will be sent by mail to schools within London and the South East to be read by Head Teachers, Premises Managers and Business Managers.

Industry/Entity Type

School

Requirements
Must have
• Schools recieve many many brochures and mail shots. Mine needs to stand out grab their attention. I have always heard that yellow is a good colour for attracting attention but you all probably know what works best.

Contact Information must be large-ish and clear on the front page.

Photos in word document must be used somewhere

Logo (Obviously)

Submissions must be of all pages otherwise they will be eliminated.
Should not have
• I don''t want before pictures on the front cover as I think it detracts and looks a but grubby.

```html
<!DOCTYPE html>
<html lang="en">
<head>
<meta charset="utf-8">
<title>Lumen School Works – Brochure Layout</title>
<link href="https://fonts.googleapis.com/css2?family=Poppins:wght@400;500;600&family=Arimo:wght@400;700&display=swap" rel="stylesheet">
<style>
:root{
  --orange:#f7a21b;
  --orange-deep:#f39200;
  --orange-soft:#fbbf5a;
  --ink:#2b2b2b;
  --grey:#555;
  --grey-band:#6d6a66;
  --red:#e2231a;
  --white:#fff;
}
*{box-sizing:border-box;margin:0;padding:0}
html,body{width:1041px;height:1200px;overflow:hidden;background:#f2f2f2}
body{position:relative;font-family:"Arimo",Arial,sans-serif;color:var(--ink)}
.page{position:absolute;overflow:hidden;box-shadow:0 1px 4px rgba(0,0,0,.18)}
.photo{position:absolute}
.brand-name{font-family:"Poppins",sans-serif;font-weight:600;color:var(--ink);display:flex;align-items:center;gap:8px;white-space:nowrap}
.brand-dot{width:14px;height:14px;border-radius:50%;background:var(--orange);flex:none}

/* ---------- front cover ---------- */
.front{left:110px;top:16px;width:400px;height:566px;background:var(--orange)}
.front .photo-playground{left:200px;top:0;width:200px;height:205px;background:linear-gradient(90deg,rgba(247,162,27,1) 0%,rgba(247,162,27,0) 35%),linear-gradient(180deg,#b9d4ec 0%,#e4eef6 35%,#b98555 60%,#6f9a3c 100%)}
.front .photo-pool{left:200px;top:205px;width:200px;height:190px;background:linear-gradient(90deg,rgba(247,162,27,1) 0%,rgba(247,162,27,0) 40%),linear-gradient(180deg,#eef0f2 0%,#dfe2e4 50%,#8c8f7c 75%,#6f7d66 100%)}
.front .photo-washroom{left:200px;top:395px;width:200px;height:171px;background:linear-gradient(90deg,rgba(247,162,27,1) 0%,rgba(247,162,27,0) 40%),linear-gradient(180deg,#d9dde6 0%,#f1f1f1 40%,#2f4f9a 70%,#23366f 100%)}
.front .logo-panel{position:absolute;left:0;top:12px;width:230px;height:84px;background:var(--white);padding:0 16px;display:flex;align-items:center}
.front .logo-panel .brand-name{font-size:16px}
.front .intro{position:absolute;left:28px;top:112px;width:200px;padding-left:10px;border-left:3px solid var(--grey);font-family:"Poppins",sans-serif;font-weight:600;font-size:12.5px;line-height:1.25;color:var(--white)}
.front .services-title{position:absolute;left:28px;top:214px;font-family:"Poppins",sans-serif;font-weight:500;font-size:16px;color:var(--white)}
.front .services-list{position:absolute;left:30px;top:240px;width:200px;list-style:none;font-family:"Poppins",sans-serif;font-size:7.8px;font-weight:500;line-height:10.2px;color:var(--ink)}
.front .services-list li{padding-left:10px;position:relative}
.front .services-list li::before{content:"";position:absolute;left:0;top:4px;width:3px;height:3px;border-radius:50%;background:var(--ink)}
.front .contact{position:absolute;left:0;top:474px;width:252px;height:92px;background:var(--white);padding:12px 0 0 26px}
.contact-lines{border-left:3px solid var(--orange);padding-left:10px;font-family:"Poppins",sans-serif;color:var(--grey);white-space:nowrap}
.contact-lines b{color:var(--ink);font-weight:600}
.front .contact-lines{font-size:9.5px;line-height:16px}

/* ---------- back cover ---------- */
.back{left:530px;top:16px;width:400px;height:566px;background:var(--orange)}
.back .art-top{left:0;top:0;width:400px;height:70px;background:linear-gradient(180deg,var(--orange-deep),var(--orange))}
.back .photo-strip{position:absolute;left:6px;top:62px;width:388px;height:108px;display:flex;gap:3px}
.back .photo-strip div{flex:1}
.back .photo-sensory{background:linear-gradient(180deg,#e9e6e2 0%,#d8cfc6 60%,#8e6e5c 100%)}
.back .photo-trampoline{background:linear-gradient(180deg,#3a8fc9 0%,#b55a3b 45%,#3e3e3e 75%,#f2b01d 100%)}
.back .photo-hygiene{background:linear-gradient(180deg,#f1efe6 0%,#ddd7c8 50%,#f5d12b 100%)}
.back .art-steps{left:200px;top:205px;width:200px;height:255px;background:linear-gradient(160deg,var(--orange-soft) 0%,var(--orange) 70%)}
.back .client-title{position:absolute;left:26px;top:196px;font-family:"Poppins",sans-serif;font-weight:500;font-size:17px;color:var(--white)}
.back .client-list{position:absolute;left:28px;top:226px;list-style:none;font-family:"Poppins",sans-serif;font-weight:500;font-size:8.4px;line-height:10.9px;color:var(--ink)}
.back .contact-title{position:absolute;left:26px;top:424px;font-family:"Poppins",sans-serif;font-weight:500;font-size:17px;color:var(--white)}
.back .address{position:absolute;left:28px;top:452px;font-family:"Poppins",sans-serif;font-weight:500;font-size:8px;line-height:11px;color:var(--ink)}
.back .footer{position:absolute;left:0;top:484px;width:400px;height:82px;background:var(--white);display:flex;align-items:center;justify-content:space-between;padding:0 16px 0 14px}
.back .footer .contact-lines{font-size:9px;line-height:15px}
.back .footer .brand-name{font-size:12.5px;gap:6px}
.back .footer .brand-dot{width:11px;height:11px}

/* ---------- inside spread ---------- */
.inside{left:120px;top:614px;width:800px;height:566px;background:var(--white)}
.inside-left{position:absolute;left:0;top:0;width:400px;height:566px;padding:12px 22px 0 22px;border-top:4px solid var(--grey-band)}
.inside-left .brand-name{font-size:14px;margin-bottom:10px}
.inside-left .lead{border-left:2px solid var(--grey);padding-left:7px;font-weight:700;font-size:8.4px;line-height:11.4px;color:var(--red);padding-bottom:2px}
.inside-left hr{border:0;border-top:1px solid #b9b9b9;margin:7px 0 9px}
.inside-left p{font-size:7.9px;line-height:11.2px;color:var(--grey);margin-bottom:9px}
.inside-left h2{font-family:"Poppins",sans-serif;font-weight:500;font-size:13px;color:var(--grey);margin:2px 0 6px}
.inside-left ul{list-style:none;margin:0 0 9px 2px;font-size:7.9px;line-height:11.2px;color:var(--grey)}
.inside-left ul li::before{content:"•";margin-right:8px}
.inside-left .bottom-band{position:absolute;left:0;bottom:0;width:400px;height:12px;background:var(--grey-band)}
.inside-right{position:absolute;left:400px;top:0;width:400px;height:566px;background:var(--orange);border-top:4px solid var(--grey-band);padding:10px 12px 0 14px}
.inside-right .art-base{left:0;top:476px;width:400px;height:90px;background:linear-gradient(180deg,var(--orange) 0%,#a88a63 55%,var(--grey-band) 100%)}
.compare{position:relative;display:flex;height:152px;margin-bottom:7px;border:2px solid var(--white);background:var(--white)}
.compare .tag{width:12px;position:relative;background:var(--white)}
.compare .tag span{position:absolute;left:50%;font-family:"Arimo",sans-serif;font-weight:700;font-size:6.5px;color:var(--ink);letter-spacing:.3px;white-space:nowrap;transform:translateX(-50%) rotate(-90deg)}
.compare .tag-before span{top:16px}
.compare .tag-after span{bottom:14px}
.compare .shot{flex:1;position:relative}
.row-1 .before{background:linear-gradient(180deg,#eef2f5 0%,#c9ccc9 35%,#7b7c7a 60%,#5a5b5c 100%)}
.row-1 .after{background:linear-gradient(180deg,#4d8ed0 0%,#b8d3ec 35%,#b07944 55%,#5f8d33 100%)}
.row-2 .before{background:linear-gradient(180deg,#8a7a3a 0%,#c9b34a 40%,#d3bd52 70%,#9c8a3c 100%)}
.row-2 .after{background:linear-gradient(180deg,#f3f3f3 0%,#dfe4ea 40%,#3b5aa4 75%,#2b3f79 100%)}
.row-3 .before{background:linear-gradient(180deg,#e8e1b5 0%,#efe7c0 45%,#b8532d 80%,#8f3b20 100%)}
.row-3 .after{background:linear-gradient(180deg,#eef1f5 0%,#c8d4e2 40%,#3fa7c7 65%,#24427d 100%)}
</style>
</head>
<body>

<section class="page front" aria-label="Front cover">
  <div class="photo photo-playground" role="img" aria-label="Photo: finished school playground with timber seating and lawn"></div>
  <div class="photo photo-pool" role="img" aria-label="Photo: accessible hydrotherapy pool room with hoist"></div>
  <div class="photo photo-washroom" role="img" aria-label="Photo: refurbished children's washroom with blue basins"></div>

  <div class="logo-panel"><div class="brand-name"><span class="brand-dot"></span>Lumen School Works</div></div>

  <p class="intro">LSW provides construction, design and project management services to schools and the wider education sector.</p>

  <h2 class="services-title">Services</h2>
  <ul class="services-list">
    <li>Receptions</li>
    <li>Toilet Areas</li>
    <li>Classrooms</li>
    <li>Corridors</li>
    <li>Staff Rooms</li>
    <li>Food Technology</li>
    <li>Design Technology</li>
    <li>ICT Suites</li>
    <li>Libraries</li>
    <li>Halls and Sports halls</li>
    <li>Specialist Special Needs Rooms</li>
    <li>Changing rooms</li>
    <li>Sensory rooms</li>
    <li>Therapy pools</li>
    <li>Hoist Installations</li>
    <li>Access and DDA Compliance</li>
    <li>General buildings maintenance</li>
    <li>Playground design.</li>
    <li>Playground equipment, surfacing and bespoke structures</li>
    <li>Temporary buildings and classrooms</li>
  </ul>

  <div class="contact">
    <div class="contact-lines">
      Tel: <b>0845 000 4417</b><br>
      Fax: <b>0845 000 4417</b><br>
      Email: <b>info@lumenschoolworks.co.uk</b><br>
      Web: <b>www.lumenschoolworks.co.uk</b>
    </div>
  </div>
</section>

<section class="page back" aria-label="Back cover">
  <div class="photo art-top" role="img" aria-label="Line drawing of timber playground seating"></div>
  <div class="photo-strip">
    <div class="photo-sensory" role="img" aria-label="Photo: sensory room with soft seating"></div>
    <div class="photo-trampoline" role="img" aria-label="Photo: playground with sunken trampoline"></div>
    <div class="photo-hygiene" role="img" aria-label="Photo: hygiene room with changing bed"></div>
  </div>
  <div class="photo art-steps" role="img" aria-label="Line drawing of timber steps and decking"></div>

  <h2 class="client-title">Client list</h2>
  <ul class="client-list">
    <li>Ashgrove Primary School ++++</li>
    <li>Little Acorns Nursery +++++</li>
    <li>Bramble Lane Nursery ++++</li>
    <li>Hillcrest School ++++</li>
    <li>Thomas Ellery Primary ++++</li>
    <li>Meridian School +++</li>
    <li>Larkfield Primary School ++++</li>
    <li>Elmstead School +++++</li>
    <li>Westbrook Primary ++++</li>
    <li>Orchard Vale Primary School ++++</li>
    <li>Kingsmere Primary School ++++</li>
    <li>Brookside Primary School +++++</li>
    <li>Borough of Eastmere +++++</li>
    <li>Borough of Northfield +++++</li>
    <li>Borough of Harbourside +++++</li>
    <li>Borough of Southgate +++++</li>
  </ul>

  <h2 class="contact-title">Contact Information</h2>
  <p class="address">Lumen School Works Limited<br>Fernhill House, Marsh Lane, Ashcombe, Surrey, KT99 1ZZ</p>

  <div class="footer">
    <div class="contact-lines">
      Tel: <b>0845 000 4417</b><br>
      Fax: <b>0845 000 4417</b><br>
      Email: <b>info@lumenschoolworks.co.uk</b><br>
      Web: <b>www.lumenschoolworks.co.uk</b>
    </div>
    <div class="brand-name"><span class="brand-dot"></span>Lumen School Works</div>
  </div>
</section>

<section class="page inside" aria-label="Inside spread">
  <div class="inside-left">
    <div class="brand-name"><span class="brand-dot"></span>Lumen School Works</div>
    <p class="lead">As a company we are passionate about the environment and our social responsibility. Wherever possible all construction materials are purchased from sustainable sources and our designs encompass many carbon and energy reducing elements as standard.</p>
    <hr>
    <p>LSW and our employees organise many fundraising activities throughout the year the proceeds of which support charities and projects in developing countries. We are an equal opportunities employer that provides a professional environment that is challenging, rewarding, creative and respectful of ideas and individuals.</p>
    <p>As a client you are always our number one priority and will enjoy unrivalled levels of service, integrity and reliability. Our projects are always carried out to the highest quality, at an agreed fixed cost and within the agreed time.</p>
    <h2>Services</h2>
    <p><b>LSW</b> provides a detailed design service. By working in partnership with the Head Teachers and Team Leaders we are able to capture and interpret your vision for the works required. Design services we can offer include,</p>
    <ul>
      <li>Full Planning Permission Applications</li>
      <li>Single / Multiple Room Refurbishments</li>
      <li>Playground Design</li>
      <li>Furniture / Workspace Design and Layout</li>
    </ul>
    <p><b>LSW</b> offer a dedicated Project Management Service aimed at schools having works carried out by BSF Local Authority contractors. When appointed we represent the school offering Technical, Financial and Project Management support to the Head teacher and Governors ensuring projects are delivered to your specification, within budget and on time</p>
    <div class="bottom-band"></div>
  </div>

  <div class="inside-right">
    <div class="photo art-base" role="img" aria-label="Line drawing of timber playground structure"></div>
    <div class="compare row-1">
      <div class="tag tag-before"><span>BEFORE</span></div>
      <div class="shot before" role="img" aria-label="Photo: bare tarmac playground before works"></div>
      <div class="shot after" role="img" aria-label="Photo: playground after works with lawn and timber seating"></div>
      <div class="tag tag-after"><span>AFTER</span></div>
    </div>
    <div class="compare row-2">
      <div class="tag tag-before"><span>BEFORE</span></div>
      <div class="shot before" role="img" aria-label="Photo: dated yellow toilet block before refurbishment"></div>
      <div class="shot after" role="img" aria-label="Photo: refurbished toilets with colourful cubicles"></div>
      <div class="tag tag-after"><span>AFTER</span></div>
    </div>
    <div class="compare row-3">
      <div class="tag tag-before"><span>BEFORE</span></div>
      <div class="shot before" role="img" aria-label="Photo: old washroom with small basins and red floor"></div>
      <div class="shot after" role="img" aria-label="Photo: new washroom with blue vanity and cubicles"></div>
      <div class="tag tag-after"><span>AFTER</span></div>
    </div>
  </div>
</section>

</body>
</html>
```